Looking for a creative label design for our retail coffee bags

We are a coffee manufacturer (coffee roaster) looking to re-brand our retail label for our coffee bags. Our main coffee blend that we sell is our Harborline Velvet Blend. You can use this name when creating the label. We are going for a look that represents our company as a coffee roaster. Please reference our website (www.brindlemugworks.com) and our Facebook page to learn more about our company and to give you more inspiration on creating this design.

Target Market(s)

Retail customers/grocery stores

Industry/Entity Type

Manufacturer

Requirements
Must have
• The size of the label has to be 3" width x 4" height

Logo must be Black
Nice to have
• We currently incorporate a color on our labels for each blend. For example, Harborline Velvet Blend (royal blue), Decaffeinated Blend (red), Breakfast Blend (green), Flavored coffees (gold).

Rustic/vintage style

```html
<!DOCTYPE html>
<html lang="en">
<head>
<meta charset="utf-8">
<title>Brindle Mugworks – Retail Coffee Labels</title>
<link href="https://fonts.googleapis.com/css2?family=Rubik:wght@500;700&family=Barlow+Condensed:wght@700&display=swap" rel="stylesheet">
<style>
  :root {
    --backdrop: #efe5d6;
    --label-black: #1d1d1d;
    --damask: #2a2a2a;
    --ink-white: #ffffff;
    --logo-black: #111111;
    --cup-gold-dark: #8a6424;
    --cup-gold-light: #e8c77c;

    --green-dark: #0b5e30;
    --green-light: #00a04e;
    --gold-dark: #5a3a1a;
    --gold-light: #f3e6cf;
    --blue-dark: #1a236b;
    --blue-light: #3346ad;
    --red-dark: #7e0d15;
    --red-light: #e4202b;
  }

  * { box-sizing: border-box; margin: 0; padding: 0; }

  html, body {
    width: 1200px;
    height: 880px;
    overflow: hidden;
    background: var(--backdrop);
  }

  .label-range {
    width: 1200px;
    height: 880px;
    display: flex;
    align-items: center;
    justify-content: center;
    gap: 24px;
  }

  .label {
    position: relative;
    width: 270px;
    height: 360px;
    background: var(--label-black);
    overflow: hidden;
    color: var(--ink-white);
    font-family: "Rubik", sans-serif;
  }

  .label--breakfast { --band-dark: var(--green-dark); --band-light: var(--green-light); }
  .label--flavored  { --band-dark: var(--gold-dark);  --band-light: var(--gold-light); }
  .label--velvet    { --band-dark: var(--blue-dark);  --band-light: var(--blue-light); }
  .label--decaf     { --band-dark: var(--red-dark);   --band-light: var(--red-light); }

  .label__pattern {
    position: absolute;
    inset: 0;
    background: radial-gradient(circle at 50% 45%, var(--damask), var(--label-black) 75%);
  }

  .label__band {
    position: absolute;
    left: 0;
    right: 0;
    height: 34px;
    background: linear-gradient(90deg,
      var(--band-dark) 0%, var(--band-light) 22%, var(--band-dark) 45%,
      var(--band-light) 68%, var(--band-dark) 85%, var(--band-light) 100%);
  }
  .label__band--top { top: 0; }
  .label__band--bottom { bottom: 0; height: 30px; }

  .label__content {
    position: relative;
    height: 100%;
    display: flex;
    flex-direction: column;
    align-items: center;
    padding-top: 50px;
  }

  .brand-mark {
    width: 98px;
    height: 98px;
    border-radius: 50%;
    background: var(--ink-white);
    display: flex;
    align-items: center;
    justify-content: center;
    text-align: center;
  }
  .brand-mark__name {
    color: var(--logo-black);
    font-family: "Rubik", sans-serif;
    font-weight: 500;
    font-size: 14px;
    line-height: 1.1;
    letter-spacing: 0.5px;
  }

  .brand-tagline {
    margin-top: 5px;
    font-size: 6px;
    font-weight: 500;
    letter-spacing: 0.6px;
    text-transform: uppercase;
    opacity: 0.85;
  }

  .blend-name {
    margin-top: 20px;
    min-height: 40px;
    padding: 0 14px;
    font-weight: 700;
    font-size: 15px;
    line-height: 1.2;
    letter-spacing: 0.3px;
    text-transform: uppercase;
    text-align: center;
  }

  .cup-art {
    margin-top: 8px;
    width: 44px;
    height: 56px;
    border-radius: 40% 40% 50% 50%;
    background: linear-gradient(160deg, var(--cup-gold-light), var(--cup-gold-dark));
    opacity: 0.9;
  }

  .label__footer {
    position: absolute;
    left: 0;
    right: 0;
    bottom: 42px;
    display: flex;
    align-items: center;
    justify-content: center;
  }

  .anniversary-seal {
    position: absolute;
    left: 16px;
    bottom: -4px;
    width: 30px;
    height: 30px;
    border-radius: 50%;
    background: var(--logo-black);
    border: 2px solid var(--cup-gold-light);
  }

  .net-weight {
    display: flex;
    align-items: center;
    gap: 7px;
    font-family: "Barlow Condensed", sans-serif;
    font-weight: 700;
    font-size: 18px;
  }

  .bean-icon { width: 14px; height: 12px; }
</style>
</head>
<body>
<main class="label-range">

  <article class="label label--breakfast">
    <div class="label__pattern" role="img" aria-label="Dark damask floral pattern background"></div>
    <div class="label__band label__band--top"></div>
    <div class="label__band label__band--bottom"></div>
    <div class="label__content">
      <div class="brand-mark"><span class="brand-mark__name">Brindle<br>Mugworks</span></div>
      <p class="brand-tagline">Proudly roasted in Harbor Point since 1994</p>
      <h2 class="blend-name">Breakfast Blend</h2>
      <div class="cup-art" role="img" aria-label="Gold ribbon illustration of a steaming coffee cup"></div>
    </div>
    <div class="label__footer">
      <div class="anniversary-seal"></div>
      <p class="net-weight">
        <svg class="bean-icon" viewBox="0 0 14 12"><ellipse cx="4" cy="7" rx="3" ry="4" fill="#fff"/><ellipse cx="10" cy="5" rx="3" ry="4" fill="#fff"/><path d="M4 3.5v7M10 1.5v7" stroke="#1d1d1d" stroke-width="0.8"/></svg>
        16 oz
        <svg class="bean-icon" viewBox="0 0 14 12"><ellipse cx="4" cy="5" rx="3" ry="4" fill="#fff"/><ellipse cx="10" cy="7" rx="3" ry="4" fill="#fff"/><path d="M4 1.5v7M10 3.5v7" stroke="#1d1d1d" stroke-width="0.8"/></svg>
      </p>
    </div>
  </article>

  <article class="label label--flavored">
    <div class="label__pattern" role="img" aria-label="Dark damask floral pattern background"></div>
    <div class="label__band label__band--top"></div>
    <div class="label__band label__band--bottom"></div>
    <div class="label__content">
      <div class="brand-mark"><span class="brand-mark__name">Brindle<br>Mugworks</span></div>
      <p class="brand-tagline">Proudly roasted in Harbor Point since 1994</p>
      <h2 class="blend-name">Flavored Coffees</h2>
      <div class="cup-art" role="img" aria-label="Gold ribbon illustration of a steaming coffee cup"></div>
    </div>
    <div class="label__footer">
      <div class="anniversary-seal"></div>
      <p class="net-weight">
        <svg class="bean-icon" viewBox="0 0 14 12"><ellipse cx="4" cy="7" rx="3" ry="4" fill="#fff"/><ellipse cx="10" cy="5" rx="3" ry="4" fill="#fff"/><path d="M4 3.5v7M10 1.5v7" stroke="#1d1d1d" stroke-width="0.8"/></svg>
        16 oz
        <svg class="bean-icon" viewBox="0 0 14 12"><ellipse cx="4" cy="5" rx="3" ry="4" fill="#fff"/><ellipse cx="10" cy="7" rx="3" ry="4" fill="#fff"/><path d="M4 1.5v7M10 3.5v7" stroke="#1d1d1d" stroke-width="0.8"/></svg>
      </p>
    </div>
  </article>

  <article class="label label--velvet">
    <div class="label__pattern" role="img" aria-label="Dark damask floral pattern background"></div>
    <div class="label__band label__band--top"></div>
    <div class="label__band label__band--bottom"></div>
    <div class="label__content">
      <div class="brand-mark"><span class="brand-mark__name">Brindle<br>Mugworks</span></div>
      <p class="brand-tagline">Proudly roasted in Harbor Point since 1994</p>
      <h2 class="blend-name">Harborline Velvet<br>Blend</h2>
      <div class="cup-art" role="img" aria-label="Gold ribbon illustration of a steaming coffee cup"></div>
    </div>
    <div class="label__footer">
      <div class="anniversary-seal"></div>
      <p class="net-weight">
        <svg class="bean-icon" viewBox="0 0 14 12"><ellipse cx="4" cy="7" rx="3" ry="4" fill="#fff"/><ellipse cx="10" cy="5" rx="3" ry="4" fill="#fff"/><path d="M4 3.5v7M10 1.5v7" stroke="#1d1d1d" stroke-width="0.8"/></svg>
        16 oz
        <svg class="bean-icon" viewBox="0 0 14 12"><ellipse cx="4" cy="5" rx="3" ry="4" fill="#fff"/><ellipse cx="10" cy="7" rx="3" ry="4" fill="#fff"/><path d="M4 1.5v7M10 3.5v7" stroke="#1d1d1d" stroke-width="0.8"/></svg>
      </p>
    </div>
  </article>

  <article class="label label--decaf">
    <div class="label__pattern" role="img" aria-label="Dark damask floral pattern background"></div>
    <div class="label__band label__band--top"></div>
    <div class="label__band label__band--bottom"></div>
    <div class="label__content">
      <div class="brand-mark"><span class="brand-mark__name">Brindle<br>Mugworks</span></div>
      <p class="brand-tagline">Proudly roasted in Harbor Point since 1994</p>
      <h2 class="blend-name">Decaffeinated Blend</h2>
      <div class="cup-art" role="img" aria-label="Gold ribbon illustration of a steaming coffee cup"></div>
    </div>
    <div class="label__footer">
      <div class="anniversary-seal"></div>
      <p class="net-weight">
        <svg class="bean-icon" viewBox="0 0 14 12"><ellipse cx="4" cy="7" rx="3" ry="4" fill="#fff"/><ellipse cx="10" cy="5" rx="3" ry="4" fill="#fff"/><path d="M4 3.5v7M10 1.5v7" stroke="#1d1d1d" stroke-width="0.8"/></svg>
        16 oz
        <svg class="bean-icon" viewBox="0 0 14 12"><ellipse cx="4" cy="5" rx="3" ry="4" fill="#fff"/><ellipse cx="10" cy="7" rx="3" ry="4" fill="#fff"/><path d="M4 1.5v7M10 3.5v7" stroke="#1d1d1d" stroke-width="0.8"/></svg>
      </p>
    </div>
  </article>

</main>
</body>
</html>
```